QDN Advisory needs business card

Having just developed a logo, I now want to use that logo in the development of a business card. The card should contain the logo, my name, title, phone, email, website and physical address. I would like to use one side of the card for details and the other side for logo and messaging. Use your creativity to place the information effectively. I want the logo to appear in a strong blue, which may be matched on the back side of the card, where the logo might be reversed out in white. I want the text to be in either dark blue or black (not light blue or gray).
I am consultant, primarily helping small and mid-size companies refine their strategy, reorganize their staff and propel forward in their industry. I also teach at universities and coach on a one-on-one basis. The final design should reflect expertise, guidance, judgement, perspective, experience.
The font used in the logo is ACaslonPro.

Target Market(s)

small to mid-size companies in the US seeking business guidance

Industry/Entity Type

Business

Font styles to use
Other font styles liked:
• ACaslonPro

Colors
0455a3
0255a3
3277b5

Requirements
Must have
• Card must convey my name and information clearly. Do not make it too small - many of my customers are 50+ years old. Please use all three of my titles: consultant / coach / instructor.
Should not have
• Please do not use icons to represent the phone, email, web. Do not use p / e / w either to indicate those details.

I have decided that a swatch of color, especially a "blue wave," does not work for me. I would rather have a simpler, more reserved look rather than a very contemporary, high color card.

Please do not deconstruct the logo or put it in a different font or italics.

```html
<!DOCTYPE html>
<html lang="en">
<head>
<meta charset="utf-8">
<title>QDN Advisory – Business Card</title>
<link rel="stylesheet" href="https://fonts.googleapis.com/css2?family=Noto+Serif:wght@400;700&family=Open+Sans:wght@400;600&display=swap">
<style>
  :root {
    --stage: #ececec;
    --card-white: #ffffff;
    --blue-strong: #0455a3;
    --blue-mid: #3277b5;
    --blue-light: #5a9fe6;
    --blue-bright: #74b0f2;
    --blue-pale: #a9d0f8;
    --ink-dark: #062a57;
    --divider: #111111;
  }
  * { box-sizing: border-box; margin: 0; padding: 0; }
  html, body {
    width: 1200px; height: 462px; overflow: hidden;
    background: var(--stage);
  }
  .canvas { position: relative; width: 1200px; height: 462px; }
  .card {
    position: absolute; top: 61px;
    width: 560px; height: 340px;
    border-radius: 18px; overflow: hidden;
    box-shadow: 0 4px 14px rgba(0,0,0,.18);
  }
  /* Front */
  .card-front { left: 20px; display: flex; background: var(--card-white); }
  .front-brand {
    width: 252px; height: 100%;
    display: flex; align-items: center; justify-content: center;
    background: var(--card-white);
  }
  .brand-name {
    display: flex; align-items: center; gap: 9px;
    font-family: "Noto Serif", serif; font-weight: 400;
    font-size: 27px; color: var(--blue-strong); line-height: 1.1;
    white-space: nowrap;
  }
  .brand-mark { width: 15px; height: 15px; background: var(--blue-strong); flex: none; }
  .front-divider {
    width: 5px; height: 100%;
    background: linear-gradient(to right, var(--blue-mid), var(--divider) 50%, var(--blue-mid));
  }
  .front-details {
    flex: 1; height: 100%;
    background: linear-gradient(135deg, var(--blue-light), var(--blue-bright) 60%, var(--blue-pale));
    color: var(--ink-dark);
    font-family: "Noto Serif", serif;
    padding: 60px 20px 0 26px;
  }
  .person-name { font-size: 20px; font-weight: 700; letter-spacing: .2px; }
  .person-title { font-size: 13px; margin-top: 3px; }
  .contact-list { list-style: none; margin-top: 46px; font-size: 15px; line-height: 1.5; }
  .address { margin-top: 38px; font-size: 15px; line-height: 1.55; }
  /* Back */
  .card-back {
    left: 620px;
    background: radial-gradient(ellipse at 50% 50%, var(--blue-bright), var(--blue-light) 70%, var(--blue-mid));
    display: flex; flex-direction: column; align-items: center; justify-content: center;
  }
  .back-name {
    display: flex; align-items: center; gap: 16px;
    font-family: "Noto Serif", serif; font-weight: 400;
    font-size: 60px; color: var(--card-white); line-height: 1;
    white-space: nowrap;
  }
  .back-name .brand-mark { width: 28px; height: 28px; background: var(--card-white); }
  .back-web {
    margin-top: 30px;
    font-family: "Open Sans", sans-serif; font-size: 19px; font-weight: 600;
    color: var(--ink-dark); letter-spacing: .5px;
  }
</style>
</head>
<body>
<main class="canvas">
  <section class="card card-front" aria-label="Card front">
    <div class="front-brand">
      <div class="brand-name"><span class="brand-mark"></span>QDN Advisory</div>
    </div>
    <div class="front-divider"></div>
    <div class="front-details">
      <p class="person-name">M. Dana Whitfield</p>
      <p class="person-title">Consultant, Coach &amp; Instructor</p>
      <ul class="contact-list">
        <li>407-555-0182</li>
        <li>dana@qdn-advisory.com</li>
        <li>www.qdn-advisory.com</li>
      </ul>
      <p class="address">1420 Larkspur Lane Orlando<br>FL 32801</p>
    </div>
  </section>

  <section class="card card-back" aria-label="Card back">
    <div class="back-name"><span class="brand-mark"></span>QDN Advisory</div>
    <p class="back-web">www.qdn-advisory.com</p>
  </section>
</main>
</body>
</html>
```